Healthy diet charts design

4 pages separate not like a single flyer. I want to create a health education resources for my company Cloverbrook Health Care.
I am attaching some files for ideas and content but we need to create a unique I like design some charts food charts and
1. right eating habits
2. principles of eating
3. Food pyramid
4. green, yellow and red foods
with the creative design but our branding cloverbrook health care
and
CLOVERBROOK Acronym
Health principles
R - Right Nutrition
E - Exercise
S - Sunlight
T - Temperance
O - Optimal water intake
R - Rest
A - Air
T - Trust in divine power
I - Initiating social support
O - Optimism
N - New beginning
It still do not match my expectation.
usa
health care

```html
<!DOCTYPE html>
<html lang="en">
<head>
<meta charset="utf-8">
<title>Cloverbrook Health Care – Eating Habits &amp; Food Codes</title>
<link href="https://fonts.googleapis.com/css2?family=Lexend:wght@300;400;500;600;700&display=swap" rel="stylesheet">
<style>
  :root{
    --purple:#6a3f9a;
    --purple-light:#7d55ad;
    --green:#7fc350;
    --green-dark:#4fa23a;
    --teal:#0aa88a;
    --navy:#1e2b4a;
    --ink:#222;
    --row-grey:#eeeeee;
    --bg:#ffffff;
  }
  *{margin:0;padding:0;box-sizing:border-box}
  html,body{width:1200px;height:558px;overflow:hidden;background:var(--bg);font-family:"Lexend",sans-serif}
  .canvas{position:relative;width:1200px;height:558px}
  .page{position:absolute;top:85px;width:549px;height:388px;background:#fff;box-shadow:0 6px 18px rgba(0,0,0,.18);overflow:hidden}
  .page--habits{left:39px}
  .page--codes{left:619px}

  .title-band{position:absolute;top:0;height:52px;background:var(--purple);color:#fff;font-weight:600;display:flex;align-items:center;justify-content:center}
  .page--habits .title-band{left:60px;width:428px;border-radius:0 0 46px 46px;font-size:15.5px}
  .page--codes .title-band{left:164px;width:385px;border-radius:0 0 0 46px;font-size:19.5px}

  .dash-frame{position:absolute;left:15px;top:17px;width:518px;height:360px;border:1px dashed #8a6fb5;border-radius:16px}
  .connectors{position:absolute;left:0;top:0}

  .hub{position:absolute;left:229px;top:148px;width:104px;height:104px}
  .hub-name{position:absolute;left:0;top:40px;width:104px;text-align:center;color:var(--navy);font-size:9.5px;font-weight:700;line-height:1.25}

  .habit{position:absolute;display:flex;align-items:center;color:#fff;font-size:7.8px;font-weight:300;line-height:1.2}
  .habit b{font-weight:600}
  .habit--purple{background:var(--purple-light)}
  .habit--green{background:var(--green)}
  .habit--left{justify-content:flex-end;text-align:right;padding-right:26px}
  .habit--right{padding-left:26px}
  .habit--big{font-size:9px}

  .badge{position:absolute;width:49px;height:49px;margin:-24.5px 0 0 -24.5px;border-radius:50%;background:#fff;display:flex;align-items:center;justify-content:center}
  .badge--purple{border:2px dotted #8e6dbf}
  .badge--green{border:2px dotted var(--green)}
  .badge-art{width:36px;height:36px;border-radius:50%;border:4px solid}
  .badge--purple .badge-art{border-color:var(--purple);background:radial-gradient(circle,#f3e7dc 0 45%,#cfe0f2 100%)}
  .badge--green .badge-art{border-color:var(--green);background:radial-gradient(circle,#f6e2cf 0 45%,#e7f2da 100%)}

  .motto-band{position:absolute;left:0;bottom:0;width:549px;height:31px;background:var(--teal);border-radius:14px 14px 0 0;color:#fff;font-size:10.3px;font-weight:500;display:flex;align-items:center;justify-content:center}

  .brand-mark{position:absolute;left:22px;top:22px;width:82px;text-align:center;color:var(--navy);font-size:9px;font-weight:700;line-height:1.25}
  .brand-dot{width:18px;height:18px;border-radius:50%;background:var(--green-dark);margin:0 auto 4px}

  .hex-row{position:absolute;left:52px;top:73px}
  .code-table{position:absolute;left:58px;top:196px;width:458px}
  .code-row{display:grid;grid-template-columns:96px 120px 114px 128px;align-items:center;text-align:center;font-size:7.8px;color:var(--ink);line-height:1.2}
  .code-row:nth-child(even){background:var(--row-grey)}
  .code-row .label{font-weight:600;font-size:10px;color:#111}
  .row-processing{height:27px}
  .row-nutrients{height:28px}
  .row-fiber{height:25px}
  .row-sugar{height:28px}
  .row-fat{height:28px}

  .produce{position:absolute}
  .produce--left{left:0;top:212px;width:34px;height:176px;background:linear-gradient(180deg,rgba(214,50,40,.55),rgba(150,190,90,.6))}
  .produce--right{left:527px;top:232px;width:22px;height:96px;background:linear-gradient(180deg,rgba(214,50,50,.5),rgba(70,140,60,.5))}
  .produce--bottom{left:34px;top:356px;width:515px;height:32px;background:linear-gradient(90deg,rgba(120,180,70,.45),rgba(255,255,255,0) 30%,rgba(230,80,70,.4) 60%,rgba(150,200,90,.45))}
</style>
</head>
<body>
<div class="canvas">

  <section class="page page--habits">
    <div class="dash-frame"></div>
    <h1 class="title-band">Right Eating &amp; Bowel Habits for Best Health</h1>

    <svg class="connectors" width="549" height="388" aria-hidden="true">
      <g fill="none" stroke-width="1.6" stroke-dasharray="1.5 3" stroke-linecap="round">
        <line x1="281" y1="200" x2="230" y2="94" stroke="#9a7cc6"/>
        <line x1="281" y1="200" x2="172" y2="155" stroke="#7fc350"/>
        <line x1="281" y1="200" x2="180" y2="238" stroke="#9a7cc6"/>
        <line x1="281" y1="200" x2="230" y2="306" stroke="#7fc350"/>
        <line x1="281" y1="200" x2="333" y2="94" stroke="#9a7cc6"/>
        <line x1="281" y1="200" x2="379" y2="147" stroke="#7fc350"/>
        <line x1="281" y1="200" x2="410" y2="200" stroke="#9a7cc6"/>
        <line x1="281" y1="200" x2="379" y2="253" stroke="#7fc350"/>
        <line x1="281" y1="200" x2="333" y2="306" stroke="#9a7cc6"/>
      </g>
    </svg>

    <div class="habit habit--purple habit--left" style="left:44px;top:75px;width:160px;height:38px">Eat slowly. Chew food well<br>and mix with saliva</div>
    <div class="habit habit--green habit--left" style="left:32px;top:127px;width:114px;height:62px;padding-right:12px">✓ Eat Heavy Breakfast<br>✓ Moderate Lunch<br>✓ Light Dinner Preferably<br>Fruits</div>
    <div class="habit habit--purple habit--left" style="left:39px;top:219px;width:118px;height:38px;padding-right:12px">After each meal empty<br>the bowel, which contains<br>previous meal's waste</div>
    <div class="habit habit--green habit--left" style="left:44px;top:287px;width:160px;height:38px">Avoid condiments, spices, greasy<br>and fatty foods</div>

    <div class="habit habit--purple habit--right habit--big" style="left:357px;top:75px;width:159px;height:38px;padding-left:28px"><span><b>5 Hours</b> gap between<br>meals is a must</span></div>
    <div class="habit habit--green habit--right habit--big" style="left:403px;top:128px;width:113px;height:38px;padding-left:14px"><span><b>Do Not Eat</b> between<br>meals. No snacks</span></div>
    <div class="habit habit--purple habit--right habit--big" style="left:432px;top:181px;width:84px;height:38px;padding-left:8px">Avoid extreme<br>hot &amp; cold foods</div>
    <div class="habit habit--green habit--right" style="left:403px;top:234px;width:113px;height:38px;padding-left:14px">Do not drink water with<br>meals. Drink 1/2 an hour<br>before1 hour after meals</div>
    <div class="habit habit--purple habit--right habit--big" style="left:354px;top:287px;width:162px;height:38px;padding-left:28px">Avoid overeating. Eat only<br>what is required</div>

    <div class="badge badge--purple" style="left:230px;top:94px"><div class="badge-art" role="img" aria-label="Illustration of a person eating slowly"></div></div>
    <div class="badge badge--green" style="left:172px;top:155px"><div class="badge-art" role="img" aria-label="Illustration of a breakfast plate"></div></div>
    <div class="badge badge--purple" style="left:180px;top:238px"><div class="badge-art" role="img" aria-label="Illustration of the intestines"></div></div>
    <div class="badge badge--green" style="left:230px;top:306px"><div class="badge-art" role="img" aria-label="Illustration of a bowl of chillies"></div></div>
    <div class="badge badge--purple" style="left:333px;top:94px"><div class="badge-art" role="img" aria-label="Illustration of a clock"></div></div>
    <div class="badge badge--green" style="left:379px;top:147px"><div class="badge-art" role="img" aria-label="Illustration of crossed-out snacks"></div></div>
    <div class="badge badge--purple" style="left:410px;top:200px"><div class="badge-art" role="img" aria-label="Illustration of hot coffee and a croissant"></div></div>
    <div class="badge badge--green" style="left:379px;top:253px"><div class="badge-art" role="img" aria-label="Illustration of a glass of water and a meal"></div></div>
    <div class="badge badge--purple" style="left:333px;top:306px"><div class="badge-art" role="img" aria-label="Illustration of a person who has overeaten"></div></div>

    <div class="hub">
      <svg width="104" height="104" viewBox="0 0 104 104" aria-hidden="true">
        <polygon points="30,0 74,0 104,30 104,74 74,104 30,104 0,74 0,30" fill="#6a3f9a"/>
        <polygon points="35,11 69,11 93,35 93,69 69,93 35,93 11,69 11,35" fill="#fff"/>
      </svg>
      <div class="hub-name">CLOVERBROOK<br>HEALTH CARE</div>
    </div>

    <p class="motto-band">Those who will not eat and drink from principle, will not be governed by principle in other things</p>
  </section>

  <section class="page page--codes">
    <div class="produce produce--left" role="img" aria-label="Fresh produce: pepper, strawberry, avocado and greens"></div>
    <div class="produce produce--right" role="img" aria-label="Fresh produce: apple and watermelon"></div>
    <div class="produce produce--bottom" role="img" aria-label="Fresh produce: beans, apple, watermelon, limes and leafy greens"></div>

    <div class="brand-mark"><div class="brand-dot"></div>CLOVERBROOK<br>HEALTH CARE</div>
    <h2 class="title-band">Green, Yellow, &amp; Red Food Codes</h2>

    <svg class="hex-row" width="470" height="126" viewBox="0 0 470 126" aria-hidden="true">
      <defs>
        <linearGradient id="fadeWhite" x1="0" y1="0" x2="0" y2="1"><stop offset=".55" stop-color="#fff"/><stop offset="1" stop-color="#dfe3cf"/></linearGradient>
        <linearGradient id="fadeGreen" x1="0" y1="0" x2="0" y2="1"><stop offset="0" stop-color="#a6d24a"/><stop offset=".6" stop-color="#5cb43a"/><stop offset="1" stop-color="#d7e4c4"/></linearGradient>
        <linearGradient id="fadeOrange" x1="0" y1="0" x2="0" y2="1"><stop offset="0" stop-color="#f8b86a"/><stop offset=".55" stop-color="#f59a23"/><stop offset="1" stop-color="#e8e2c8"/></linearGradient>
        <linearGradient id="fadeRed" x1="0" y1="0" x2="0" y2="1"><stop offset="0" stop-color="#e23a3a"/><stop offset=".6" stop-color="#c51d25"/><stop offset="1" stop-color="#e6d8cc"/></linearGradient>
      </defs>
      <polygon points="60,0 120,31 120,93 60,124 0,93 0,31" fill="url(#fadeWhite)" stroke="#6b6b2a" stroke-width="1"/>
      <circle cx="60" cy="60" r="34" fill="#2f9e46"/>

      <polygon points="177,0 234,31 234,93 177,124 120,93 120,31" fill="url(#fadeGreen)"/>
      <circle cx="177" cy="59" r="26" fill="#6a8a2a" stroke="#4e6b1c" stroke-width="1.5"/>
      <path d="M165 60 L174 71 L190 46" fill="none" stroke="#fff" stroke-width="5" stroke-linecap="round" stroke-linejoin="round"/>

      <polygon points="291,0 348,31 348,93 291,124 234,93 234,31" fill="url(#fadeOrange)"/>
      <polygon points="291,36 317,81 265,81" fill="none" stroke="#fff" stroke-width="3" stroke-linejoin="round"/>

      <polygon points="408,0 467,31 467,93 408,124 349,93 349,31" fill="url(#fadeRed)"/>
      <polygon points="399,40 417,40 430,53 430,71 417,84 399,84 386,71 386,53" fill="none" stroke="#fff" stroke-width="4"/>
    </svg>

    <div class="code-table">
      <div class="code-row row-processing"><span class="label">PROCESSING</span><span>Least-Processed</span><span>Some Processing</span><span>Most-Processed Food</span></div>
      <div class="code-row row-nutrients"><span class="label">Nutrients</span><span>Whole Foods Nutrient<br>packed</span><span>Some Healthful Nutrients</span><span>Lower Quality<br>Ingredients</span></div>
      <div class="code-row row-fiber"><span class="label">FIBER</span><span>High in Fiber</span><span>Lowe in Fiber</span><span>Minimal Fiber</span></div>
      <div class="code-row row-sugar"><span class="label">SUGAR</span><span>Low in Added Sugar</span><span>Added Sugar or Artifical<br>Sweetners</span><span>Added Sugar or Artifical<br>Sweetners</span></div>
      <div class="code-row row-fat"><span class="label">FAT</span><span>Healthy Fats</span><span>Poor-Quality Fats</span><span>Excess Fats and/or Trans<br>Fat Fried Foods</span></div>
    </div>
  </section>

</div>
</body>
</html>
```